Real estate business card

I need a business card for my real estate company. I help clients buy and sell properties. I would like to keep the design very simple and professional. I would like the design to convey professionalism, safety and trust. I prefer no graphics but a simple logo design would be nice if that is part of what you do.
Updates

Please keep the designs simple. No high-rise buildings please. 

Reason: My design has not been finalized.

Target Market(s)

Age group 30-60 mostly affluent

Industry/Entity Type

Real Estate

Contact Information for Business Card

Velmont Realtors
Howard Prisk, Broker
4153 Marlow Ave. #226, La Crescenta, CA 91207

Requirements
Nice to have
• Logo can be combination of my initials HP or just Z or a simple geometric shape? Please see "Desig Ideas" attachment. No pics of houses or shaking hands, dollar bills, $, %, etc...
Please use fonts similar to Helvetica for a clean, modern look (think Northern European design, simple, clean yet bold)

Also use font colors such as blue, grey in different shades. Use pastel colors if better.

```html
<!DOCTYPE html>
<html lang="en">
<head>
<meta charset="utf-8">
<title>Velmont Realtors – Business Card</title>
<link rel="stylesheet" href="https://fonts.googleapis.com/css2?family=Lato:wght@400;700;900&display=swap">
<style>
  :root {
    --page-bg: #e6e7ec;
    --card-white: #ffffff;
    --brand-blue: #2e2f95;
    --text-grey: #8a8a8c;
    --name-grey: #8e8e90;
  }
  * { box-sizing: border-box; margin: 0; padding: 0; }
  html, body {
    width: 1200px;
    height: 1000px;
    overflow: hidden;
    background: var(--page-bg);
    font-family: "Lato", Helvetica, Arial, sans-serif;
  }
  .stage {
    width: 1200px;
    height: 1000px;
    display: flex;
    align-items: center;
    justify-content: center;
  }
  .business-card {
    position: relative;
    width: 1000px;
    height: 580px;
    background: var(--card-white);
    border-radius: 28px;
    overflow: hidden;
    box-shadow: 0 10px 30px rgba(0, 0, 0, 0.12);
    display: flex;
    flex-direction: column;
    align-items: center;
  }
  .brand-lockup {
    margin-top: 120px;
    display: flex;
    align-items: center;
    gap: 18px;
  }
  .brand-mark {
    width: 30px;
    height: 30px;
    background: var(--brand-blue);
  }
  .brand-name {
    font-weight: 900;
    font-size: 60px;
    letter-spacing: 2px;
    color: var(--brand-blue);
    text-transform: uppercase;
  }
  .person {
    margin-top: 60px;
    text-align: center;
  }
  .person-name {
    font-weight: 700;
    font-size: 34px;
    color: var(--name-grey);
    text-transform: uppercase;
    letter-spacing: 0.5px;
  }
  .person-title {
    font-weight: 700;
    font-size: 26px;
    color: var(--brand-blue);
    margin-top: 4px;
  }
  .office {
    margin-top: 34px;
    text-align: center;
  }
  .office-name {
    font-weight: 900;
    font-size: 30px;
    color: var(--brand-blue);
    text-transform: uppercase;
  }
  .office-address {
    font-weight: 400;
    font-size: 28px;
    color: var(--text-grey);
    margin-top: 6px;
  }
  .card-band {
    position: absolute;
    left: 0;
    right: 0;
    bottom: 0;
    height: 38px;
    background: var(--brand-blue);
  }
</style>
</head>
<body>
  <main class="stage">
    <section class="business-card">
      <div class="brand-lockup">
        <span class="brand-mark"></span>
        <span class="brand-name">Velmont Realtors</span>
      </div>
      <div class="person">
        <p class="person-name">Howard Prisk</p>
        <p class="person-title">Broker</p>
      </div>
      <div class="office">
        <p class="office-name">Velmont Realtors</p>
        <p class="office-address">4153 Marlow Ave. #226, La Crescenta, CA 91207</p>
      </div>
      <div class="card-band"></div>
    </section>
  </main>
</body>
</html>
```